Business Card Design

About Us
VaultNet is a young and innovative company focusing on security and hosting solutions for global enterprise. To supply the high-performance, highly interconnected and low latency DDoS protection service, we distributed a large number of huge scrubbing centers all over the world. So VaultNet is the first choice for enterprise to protect their network security.

Task detail
1. We hope that the business card can be filled with creativity, simple and technologe, the business card background is white, the business card text color and other colors are black, blue, green or your needs.

2. We need the source files provided by the successful bidder, such as *.psd, *.ai, etc.

3. One side contains the following:
-Logo
-Marco Sales Manager
-VAULTNET TECHNOLOGY CO., LIMITED
-Add:
9/F., Harbourgate Tower,
318 Pelton Avenue, Tsimwell, Kowloon,
HK
-Tel: 86-755-4719 2058
-Phone: 86-189 6140 3527
-Email: marco@vault-netz.example
-Web: www.vault-netz.example

4. The other side contains the following:
-Logo

5. Please find the attachment contains the logo PSD source files.

```html
<!DOCTYPE html>
<html lang="en">
<head>
<meta charset="utf-8">
<title>VaultNet Business Card</title>
<link href="https://fonts.googleapis.com/css2?family=Open+Sans:wght@400;600;700&display=swap" rel="stylesheet">
<style>
  :root {
    --backdrop: #3b3b3b;
    --card: #ffffff;
    --teal: #2fb1c6;
    --green: #6cbb3c;
    --ink: #3a3a3a;
    --ink-soft: #4a4a4a;
  }
  * { box-sizing: border-box; margin: 0; padding: 0; }
  html, body { width: 1200px; height: 1000px; overflow: hidden; }
  body {
    position: relative;
    background: var(--backdrop);
    font-family: "Open Sans", Arial, sans-serif;
    color: var(--ink);
  }
  .card {
    position: absolute;
    width: 522px;
    height: 306px;
    background: var(--card);
    box-shadow: 0 4px 14px rgba(0,0,0,0.45);
  }
  .card--front { left: 161px; top: 175px; }
  .card--back { left: 510px; top: 532px; }
  .band {
    position: absolute;
    left: 0; width: 100%;
    height: 29px;
    background: var(--teal);
  }
  .band--top { top: 0; }
  .band--bottom { bottom: 0; }

  .brand {
    position: absolute;
    display: flex;
    align-items: center;
    font-weight: 700;
    color: var(--ink);
    letter-spacing: -0.5px;
  }
  .brand__square { background: var(--teal); flex: none; }
  .card--front .brand { left: 107px; top: 108px; font-size: 52px; gap: 14px; }
  .card--front .brand__square { width: 44px; height: 44px; }
  .card--back .brand { left: 27px; top: 60px; font-size: 34px; gap: 10px; }
  .card--back .brand__square { width: 28px; height: 28px; }

  .person {
    position: absolute;
    right: 34px; top: 122px;
    text-align: right;
  }
  .person__name { font-size: 20px; font-weight: 600; color: var(--green); line-height: 24px; }
  .person__role { font-size: 12.5px; color: var(--ink-soft); line-height: 18px; }
  .rule {
    position: absolute;
    left: 27px; right: 34px; top: 168px;
    height: 2px;
    background: var(--teal);
  }
  .address {
    position: absolute;
    left: 27px; top: 197px;
    font-size: 12.5px;
    line-height: 17.5px;
    color: var(--ink-soft);
    font-style: normal;
  }
  .address__company { color: var(--green); font-weight: 600; }
  .contacts {
    position: absolute;
    right: 34px; top: 192px;
    list-style: none;
    font-size: 12.5px;
    line-height: 18px;
    color: var(--ink-soft);
  }
  .contacts li { display: flex; justify-content: flex-end; align-items: center; gap: 8px; }
  .contacts svg { width: 14px; height: 14px; flex: none; fill: var(--green); }
</style>
</head>
<body>

<section class="card card--front">
  <div class="band band--top" role="img" aria-label="Teal brick-wall pattern band"></div>
  <div class="brand"><span class="brand__square"></span>VaultNet</div>
  <div class="band band--bottom" role="img" aria-label="Teal brick-wall pattern band"></div>
</section>

<section class="card card--back">
  <div class="band band--top" role="img" aria-label="Teal brick-wall pattern band"></div>
  <div class="brand"><span class="brand__square"></span>VaultNet</div>

  <div class="person">
    <div class="person__name">Marco</div>
    <div class="person__role">Sales Manager</div>
  </div>
  <div class="rule"></div>

  <address class="address">
    <div class="address__company">VaultNet</div>
    9/F, Harbourgate Tower,<br>
    318 Pelton Avenue,<br>
    Tsimwell, Kowloon, HK
  </address>

  <ul class="contacts">
    <li>86-755-4719 2058
      <svg viewBox="0 0 16 16" aria-hidden="true"><path d="M3.6 1.2l2.3 2.6-1.3 1.9c.9 2 2.4 3.6 4.6 4.7l1.8-1.4 2.8 2.2-1.2 2.6C7.3 13.6 2.5 8.8 1.2 3z"/></svg>
    </li>
    <li>86-189 6140 3527
      <svg viewBox="0 0 16 16" aria-hidden="true"><path d="M4.5 1h7a1 1 0 0 1 1 1v12a1 1 0 0 1-1 1h-7a1 1 0 0 1-1-1V2a1 1 0 0 1 1-1zm.6 2v9h5.8V3zm2.9 9.8a.7.7 0 1 0 0 1.4.7.7 0 0 0 0-1.4z"/></svg>
    </li>
    <li>marco@vault-netz.example
      <svg viewBox="0 0 16 16" aria-hidden="true"><path d="M1 4h14v9H1zm1.4 1L8 9l5.6-4z"/></svg>
    </li>
    <li>www.vault-netz.example
      <svg viewBox="0 0 16 16" aria-hidden="true"><path d="M8 1a7 7 0 1 0 0 14A7 7 0 0 0 8 1zm0 1.5c.8 0 1.6 1.7 1.9 4.5H6.1C6.4 4.2 7.2 2.5 8 2.5zM2.6 7h2.1c.1-1.7.5-3.1 1-4A5.5 5.5 0 0 0 2.6 7zm8.7 0h2.1a5.5 5.5 0 0 0-3.1-4c.5.9.9 2.3 1 4zM2.6 9a5.5 5.5 0 0 0 3.1 4c-.5-.9-.9-2.3-1-4zm3.5 0c.3 2.8 1.1 4.5 1.9 4.5s1.6-1.7 1.9-4.5zm5.2 0c-.1 1.7-.5 3.1-1 4a5.5 5.5 0 0 0 3.1-4z"/></svg>
    </li>
  </ul>

  <div class="band band--bottom" role="img" aria-label="Teal brick-wall pattern band"></div>
</section>

</body>
</html>
```